Unique and original Business Card for Financial Services Business

I have moved premises and need to change the detail on my business card so thought now is a good time for a re-design. Looking for something professional and modern with colours to fit in with out logo. Like the idea of foil or embossing if that works but not a must have but I do want something that stands out and that I could not design myself.

Once business card is designed I will also be looking to get letterhead and flyers done but want the business card concept in place first.

The majority of designs I am receiving are generic and template based. I am looking for something unique and original. We have some great design elements in our logo, think outside the box and show me something that stands out from the crowd.

Target Market(s)

Business Professionals

Industry/Entity Type

Finance

Contact Information for Business Card

Name: Delia Norwood Phone 0473 958 162 Address PO Box 8617 Mossvale NSW 2389 Email info@steadyharbourfinancialservices.com.au website www.steadyharbourfinancialservices.com.au

Font styles to use
Other font styles liked:
• Ralway

Requirements
Should not have
• No black backgrounds please

```html
<!DOCTYPE html>
<html lang="en">
<head>
<meta charset="utf-8">
<title>Steady Harbour Financial Services – Business Card</title>
<link href="https://fonts.googleapis.com/css2?family=Roboto+Condensed:wght@300;400;700&display=swap" rel="stylesheet">
<style>
  :root {
    --stage: #e4e4e4;
    --card: #ffffff;
    --ink: #111111;
    --ink-soft: #2a2a2a;
    --teal-light: #1fa7a3;
    --teal: #12858c;
    --teal-deep: #0b4f6c;
    --grey: #9a9ca0;
  }
  * { margin: 0; padding: 0; box-sizing: border-box; }
  html, body {
    width: 1200px;
    height: 1200px;
    overflow: hidden;
    background: var(--stage);
    font-family: "Roboto Condensed", "Arial Narrow", sans-serif;
  }
  .card {
    position: absolute;
    left: 150px;
    width: 898px;
    height: 525px;
    background: var(--card);
    box-shadow: 0 2px 6px rgba(0,0,0,0.18);
    overflow: hidden;
  }
  .card--front { top: 56px; }
  .card--back { top: 616px; }

  /* Front */
  .holder-name {
    position: absolute;
    right: 389px;
    top: 116px;
    font-weight: 700;
    font-size: 50px;
    line-height: 1;
    color: var(--ink);
    letter-spacing: -0.3px;
  }
  .holder-title {
    position: absolute;
    right: 389px;
    top: 172px;
    font-weight: 300;
    font-size: 17px;
    color: var(--ink-soft);
  }
  .contact-list {
    list-style: none;
    position: absolute;
    right: 386px;
    top: 266px;
  }
  .contact-item {
    display: flex;
    justify-content: flex-end;
    align-items: center;
    height: 35px;
    font-weight: 300;
    font-size: 20px;
    color: var(--ink-soft);
  }
  .contact-item--address { margin-top: 28px; }
  .contact-icon {
    width: 14px;
    height: 14px;
    margin-left: 16px;
    flex: none;
  }
  .feature-panel {
    position: absolute;
    left: 609px;
    top: 0;
    width: 289px;
    height: 525px;
    background: linear-gradient(180deg, var(--teal-light) 0%, var(--teal) 45%, var(--teal-deep) 100%);
  }

  /* Back */
  .bird-art {
    position: absolute;
    border-radius: 50%;
    background: radial-gradient(circle at 60% 40%, var(--teal-light) 0%, var(--teal) 55%, rgba(11,79,108,0.85) 100%);
  }
  .bird-art--large { left: 112px; top: 71px; width: 257px; height: 319px; }
  .bird-art--small-top { left: 444px; top: 105px; width: 62px; height: 73px; }
  .bird-art--small-bottom { left: 288px; top: 378px; width: 60px; height: 68px; }

  .brand-name {
    position: absolute;
    left: 412px;
    top: 370px;
    width: 410px;
    text-align: center;
    font-weight: 400;
    color: var(--teal);
  }
  .brand-name__main {
    display: block;
    font-size: 47px;
    line-height: 1;
    letter-spacing: -0.5px;
    text-transform: uppercase;
  }
  .brand-name__sub {
    display: block;
    margin-top: 6px;
    font-size: 24px;
    line-height: 1;
    letter-spacing: 6px;
  }
</style>
</head>
<body>

<section class="card card--front" aria-label="Business card front">
  <h1 class="holder-name">Delia Norwood</h1>
  <p class="holder-title">Director</p>

  <ul class="contact-list">
    <li class="contact-item">0473 958 162
      <svg class="contact-icon" viewBox="0 0 14 14" aria-hidden="true"><path d="M3 1.5 L5 1.5 L6 4.5 L4.6 5.6 C5.4 7.4 6.6 8.6 8.4 9.4 L9.5 8 L12.5 9 L12.5 11 C12.5 12 11.7 12.7 10.8 12.6 C6 12 2 8 1.4 3.2 C1.3 2.3 2 1.5 3 1.5 Z" fill="#222"/></svg>
    </li>
    <li class="contact-item">info@steadyharbourfinancialservices.com.au
      <svg class="contact-icon" viewBox="0 0 14 14" aria-hidden="true"><rect x="1" y="3" width="12" height="8.5" fill="#222"/><path d="M1.5 3.5 L7 8 L12.5 3.5" fill="none" stroke="#fff" stroke-width="1.1"/></svg>
    </li>
    <li class="contact-item">www.steadyharbourfinancialservices.com.au
      <svg class="contact-icon" viewBox="0 0 14 14" aria-hidden="true"><circle cx="7" cy="7" r="6" fill="#222"/><path d="M1.5 7 H12.5 M7 1 C4.5 4 4.5 10 7 13 M7 1 C9.5 4 9.5 10 7 13" fill="none" stroke="#fff" stroke-width="0.9"/></svg>
    </li>
    <li class="contact-item contact-item--address">PO Box 8617 Mossvale NSW 2389
      <svg class="contact-icon" viewBox="0 0 14 14" aria-hidden="true"><path d="M7 1 C4.6 1 3 2.8 3 5 C3 7.6 7 11 7 11 C7 11 11 7.6 11 5 C11 2.8 9.4 1 7 1 Z" fill="#222"/><circle cx="7" cy="5" r="1.5" fill="#fff"/><rect x="2.5" y="12" width="9" height="1.2" fill="#222"/></svg>
    </li>
  </ul>

  <div class="feature-panel" role="img" aria-label="Teal panel with floral flourishes and a hummingbird silhouette"></div>
</section>

<section class="card card--back" aria-label="Business card back">
  <div class="bird-art bird-art--large" role="img" aria-label="Large teal hummingbird silhouette in flight"></div>
  <div class="bird-art bird-art--small-top" role="img" aria-label="Small teal hummingbird silhouette"></div>
  <div class="bird-art bird-art--small-bottom" role="img" aria-label="Small teal hummingbird silhouette"></div>

  <p class="brand-name">
    <span class="brand-name__main">Steady Harbour</span>
    <span class="brand-name__sub">Financial Services</span>
  </p>
</section>

</body>
</html>
```